The company Tasovel needs a design for CBD capsules

We (Tasovel) need a new design for our CBD capsules. We already have a design for CBD oil. However, we do not want to use this completely. The Plinkar label and the cans serve as a template. Please upload in the format 139mm x 59mm incl.
2mm bleed all around and in .pdf vector. The logo files for Tasovel are included in the briefing.
Updates

Industry/Entity Type

Onlineshop

Colors
00AB8E
00BBA5
67D7C9
C6EFE9
E9F9F6

Requirements
Must have
• Please in the format 139mm x 59mm incl. 2mm bleed all around and .pdf vector
Should not have
• It shouldn't be the same label, but it should be recognizable.

```html
<!DOCTYPE html>
<html lang="de">
<head>
<meta charset="utf-8">
<title>Tasovel CBD Capsules Label</title>
<link rel="stylesheet" href="https://fonts.googleapis.com/css2?family=DM+Serif+Display&family=Oswald:wght@500;700&family=Allura&family=Roboto:wght@500&display=swap">
<style>
  :root {
    --canvas: #ffffff;
    --label-teal: #1f4a56;
    --label-teal-light: #2d6470;
    --label-white: #ffffff;
    --ink-dark: #1f3d47;
    --leaf-green: #35603f;
    --leaf-dark: #1c2b22;
  }
  * { margin: 0; padding: 0; box-sizing: border-box; }
  html, body {
    width: 1193px;
    height: 1200px;
    overflow: hidden;
    background: var(--canvas);
  }
  /* 139 x 59 mm label, landscape */
  .label {
    position: absolute;
    left: 46px;
    top: 366px;
    width: 1100px;
    height: 467px;
    background: linear-gradient(90deg, var(--label-teal) 0%, var(--label-teal-light) 33%, var(--label-teal) 55%, var(--label-teal) 100%);
    overflow: hidden;
  }
  .label__wave {
    position: absolute;
    inset: 0;
    width: 100%;
    height: 100%;
  }
  .brand {
    position: absolute;
    top: 44px;
    left: 350px;
    width: 400px;
    text-align: center;
    font-family: "DM Serif Display", serif;
    font-size: 38px;
    line-height: 48px;
    color: var(--label-white);
  }
  .product {
    position: absolute;
    top: 100px;
    left: 350px;
    width: 400px;
    text-align: center;
    color: var(--label-white);
    font-family: "Oswald", sans-serif;
  }
  .product__name {
    font-weight: 700;
    font-size: 88px;
    line-height: 96px;
    letter-spacing: 1px;
  }
  .product__form {
    font-weight: 500;
    font-size: 20px;
    line-height: 26px;
    letter-spacing: 4px;
    padding-left: 4px;
  }
  .hemp-art {
    position: absolute;
    left: 565px;
    top: 236px;
    width: 150px;
    height: 96px;
    border-radius: 50%;
    background: radial-gradient(ellipse at 50% 50%, var(--leaf-dark) 0%, var(--leaf-green) 70%, var(--leaf-green) 100%);
  }
  .claims {
    position: absolute;
    left: 450px;
    top: 280px;
    list-style: none;
    font-family: "Oswald", sans-serif;
    font-weight: 500;
    font-size: 13px;
    color: var(--ink-dark);
  }
  .claims li {
    display: flex;
    align-items: center;
    gap: 5px;
    height: 21px;
  }
  .claims svg { width: 11px; height: 11px; }
  .spectrum {
    position: absolute;
    left: 420px;
    top: 334px;
    font-family: "Allura", cursive;
    font-size: 42px;
    line-height: 50px;
    color: var(--ink-dark);
  }
  .strength {
    position: absolute;
    left: 666px;
    top: 334px;
    font-family: "Roboto", sans-serif;
    font-weight: 500;
    font-size: 24px;
    line-height: 30px;
    color: var(--label-white);
  }
</style>
</head>
<body>
  <div class="label">
    <svg class="label__wave" viewBox="0 0 1100 467" preserveAspectRatio="none" aria-hidden="true">
      <path d="M0,390 C180,350 330,262 500,262 C590,262 640,330 690,467 L0,467 Z" fill="var(--label-white)"/>
    </svg>

    <div class="brand">Tasovel</div>

    <div class="product">
      <div class="product__name">CBD</div>
      <div class="product__form">CAPSULES</div>
    </div>

    <div class="hemp-art" role="img" aria-label="Hemp leaves with dark CBD capsules"></div>

    <ul class="claims">
      <li>
        <svg viewBox="0 0 22 22" aria-hidden="true"><path d="M3 12 L9 18 L19 4" fill="none" stroke="var(--ink-dark)" stroke-width="3"/></svg>
        VEGAN
      </li>
      <li>
        <svg viewBox="0 0 22 22" aria-hidden="true"><path d="M3 12 L9 18 L19 4" fill="none" stroke="var(--ink-dark)" stroke-width="3"/></svg>
        GENTECHNIK FREI
      </li>
    </ul>

    <div class="spectrum">Vollspektrum</div>
    <div class="strength">10%</div>
  </div>
</body>
</html>
```